Update a high tech public relations agency website

Hi! I am looking for a nice, clean refresh of my website. The URL is: www.brimlowcomms.example.

Here's what I'm hoping for:
*To be able to go in to the Wordpress site and change text by myself once the design is set.
*To be able to go in and create a blog.

Here are examples of designs that I like. I'd like to see something along these lines:
www.quillpatch.example
www.PinTally.example
www.TaskVane.example
www.Steadymailer.example
www.ByteLedger.example

Some other things to note that may help:
*No white text with black background.
*I'm open to different color schemes. I like blue, green and red.
Updates

Hi all, Thanks for your interest in this project. Couple of things to note: please use the subheads in blue for the text. I don't want to use inbound marketing as the lead in. The up front text should be High Tech and AdTech Public Relations. Results Driven Media Relations. Content Strategy. Also, please....no stock images of people smiling or shaking hands or doing other fake corporate activities. Graphics would be nice. Thank you.

Industry/Entity Type

Tech

```html
<!DOCTYPE html>
<html lang="en">
<head>
<meta charset="utf-8">
<title>Brimlow Communications – High Tech Public Relations</title>
<link rel="stylesheet" href="https://fonts.googleapis.com/css2?family=Gelasio:wght@400&family=Open+Sans:wght@300;400;600;700&display=swap">
<style>
  :root {
    --blue: #1a5a8f;
    --navy: #14507f;
    --green: #a4c40a;
    --red: #dd1018;
    --tag-red: #f0262a;
    --ink: #1e1e1e;
    --grey-text: #555;
    --header-bg: #f1f1f1;
    --rule: #d8d8d8;
    --white: #ffffff;
  }
  * { box-sizing: border-box; margin: 0; padding: 0; }
  html, body { width: 1089px; height: 1200px; overflow: hidden; background: var(--white); }
  body { position: relative; font-family: "Open Sans", Arial, sans-serif; color: var(--ink); }

  .site-header {
    position: absolute; left: 0; top: 0; width: 1089px; height: 100px;
    background: linear-gradient(#f6f6f6, var(--header-bg));
    border-bottom: 1px solid var(--rule);
  }
  .brand { position: absolute; left: 36px; top: 24px; color: var(--blue); font-family: "Gelasio", Georgia, serif; font-weight: 400; line-height: 1; }
  .brand-name { font-size: 34px; letter-spacing: -0.5px; display: block; }
  .brand-sub { font-size: 15px; letter-spacing: 0.4px; display: block; margin-top: 2px; }

  .main-nav a {
    position: absolute; top: 39px; font-size: 15.5px; color: var(--blue);
    text-decoration: none; line-height: 22px;
  }
  .main-nav a.is-current { border-bottom: 3px solid var(--navy); padding-bottom: 1px; }

  .social { position: absolute; left: 968px; top: 35px; display: flex; gap: 1px; }
  .social span { display: block; width: 27px; height: 27px; }
  .social .s-one { background: var(--blue); }
  .social .s-two { background: var(--navy); }
  .social .s-mail { background: #b4b4b4; }

  .hero-title {
    position: absolute; left: 0; top: 143px; width: 1089px; text-align: center;
    font-family: "Gelasio", Georgia, serif; font-weight: 400; font-size: 40px;
    letter-spacing: -1.2px; color: var(--blue);
  }
  .venn { position: absolute; left: 340px; top: 236px; }

  .cta { position: absolute; left: 454px; top: 645px; }

  .about-heading {
    position: absolute; left: 37px; top: 794px;
    font-family: "Gelasio", Georgia, serif; font-weight: 400; font-size: 43px;
    letter-spacing: -1.2px; color: var(--blue);
  }
  .learn-more { position: absolute; left: 38px; top: 853px; }

  .service-card {
    position: absolute; top: 798px; height: 267px;
    border-top: 6px solid var(--navy);
    background: radial-gradient(ellipse at 50% 40%, #ffffff 20%, #eeeeee 100%);
    padding: 0 30px 0 40px;
  }
  .service-card h3 {
    font-family: "Gelasio", Georgia, serif; font-weight: 400; font-size: 19px;
    line-height: 22px; color: var(--ink); margin-bottom: 9px;
  }
  .service-card p { font-size: 11.3px; line-height: 15.2px; color: var(--ink); }
  .service-card p + p { margin-top: 15px; }
  .card-pr { left: 236px; width: 266px; padding-top: 50px; }
  .card-media { left: 510px; width: 265px; padding-top: 61px; padding-left: 34px; }
  .card-content { left: 785px; width: 266px; padding-top: 58px; padding-left: 33px; }

  .site-footer {
    position: absolute; left: 0; top: 1144px; width: 1089px; height: 56px;
    background: var(--navy); color: var(--white);
  }
  .footer-links { position: absolute; left: 39px; top: 14px; font-size: 10px; }
  .footer-links span { margin: 0 3px; }
  .phone { position: absolute; left: 856px; top: 7px; display: flex; align-items: center; gap: 14px; }
  .phone-number { font-size: 28px; font-weight: 300; letter-spacing: -0.3px; }
</style>
</head>
<body>
  <header class="site-header">
    <div class="brand"><span class="brand-name">Brimlow</span><span class="brand-sub">COMMUNICATIONS</span></div>
    <nav class="main-nav">
      <a href="#" style="left:358px">Home</a>
      <a href="#" class="is-current" style="left:418px">About Us</a>
      <a href="#" style="left:503px">What we do</a>
      <a href="#" style="left:605px">Principal</a>
      <a href="#" style="left:685px">Services</a>
      <a href="#" style="left:761px">Contact</a>
    </nav>
    <div class="social">
      <span class="s-one"></span>
      <span class="s-two"></span>
      <svg class="s-mail" width="27" height="27" viewBox="0 0 27 27" style="display:block;background:#b4b4b4">
        <rect x="6" y="8" width="15" height="11" fill="none" stroke="#fff" stroke-width="1.4"/>
        <polyline points="6,8 13.5,14 21,8" fill="none" stroke="#fff" stroke-width="1.4"/>
      </svg>
    </div>
  </header>

  <h1 class="hero-title">High Tech Public Relations. Content Strategy.</h1>

  <svg class="venn" width="410" height="370" viewBox="0 0 410 370">
    <circle cx="124" cy="251" r="98" fill="none" stroke="var(--blue)" stroke-width="17"/>
    <circle cx="202" cy="114" r="98" fill="none" stroke="var(--green)" stroke-width="17"/>
    <circle cx="284" cy="251" r="98" fill="none" stroke="var(--red)" stroke-width="17"/>
    <!-- team icon -->
    <g fill="var(--green)">
      <circle cx="199" cy="57" r="6"/>
      <path d="M187 78 q0-12 12-12 q12 0 12 12z"/>
      <circle cx="208" cy="59" r="5"/>
      <path d="M206 66 q12 0 14 12 h-8z"/>
    </g>
    <g font-family="Open Sans, sans-serif" font-weight="700" font-size="14.5" text-anchor="middle">
      <text x="199" y="100" fill="var(--green)">Lorem Ipsum</text>
      <text x="201" y="122" fill="var(--green)">Dolor sit</text>
      <text x="120" y="267" fill="var(--blue)">Lorem Ipsum</text>
      <text x="122" y="289" fill="var(--blue)">Dolor sit</text>
      <text x="291" y="267" fill="var(--red)">Lorem Ipsum</text>
      <text x="293" y="289" fill="var(--red)">Dolor sit</text>
    </g>
    <!-- cloud icon -->
    <path d="M108 243 h29 a6 6 0 0 0 0-12 a9 9 0 0 0-16-6 a7 7 0 0 0-12 4 a7 7 0 0 0-1 14z" fill="var(--blue)"/>
    <!-- documents icon -->
    <g fill="none" stroke="var(--red)" stroke-width="1.2">
      <rect x="283" y="219" width="12" height="15"/>
      <rect x="286" y="216" width="12" height="15" fill="#fff"/>
      <rect x="289" y="213" width="12" height="15" fill="#fff"/>
      <line x1="292" y1="218" x2="298" y2="218"/>
      <line x1="292" y1="221" x2="298" y2="221"/>
      <line x1="292" y1="224" x2="298" y2="224"/>
    </g>
  </svg>

  <svg class="cta" width="180" height="41" viewBox="0 0 180 41">
    <polygon points="0,0 180,0 160,20.5 180,41 0,41 20,20.5" fill="var(--navy)"/>
    <text x="90" y="27" text-anchor="middle" font-family="Open Sans, sans-serif" font-size="18" fill="#fff">Get in Touch</text>
  </svg>

  <h2 class="about-heading">About Us</h2>
  <svg class="learn-more" width="88" height="23" viewBox="0 0 88 23">
    <polygon points="0,0 78,0 88,11.5 78,23 0,23" fill="var(--tag-red)"/>
    <text x="12" y="15.5" font-family="Open Sans, sans-serif" font-size="10.5" fill="#fff">Learn More</text>
  </svg>

  <article class="service-card card-pr">
    <h3>High Tech Public<br>Relations</h3>
    <p>Partner with an independent public relations resource or our team of independent communications pros.</p>
    <p>Each team member has a minimum of 15 years experience on both the</p>
  </article>
  <article class="service-card card-media">
    <h3>Media Relations</h3>
    <p>Our strategic approach to media relations focuses on building long-term relationships with journalists and influencers. We partner with you to develop compelling business and industry stories.</p>
  </article>
  <article class="service-card card-content">
    <h3>Content Strategy</h3>
    <p>BrimlowPR excels at writing quality content. This comes from a deep understanding of technology, digital marketing, and the challenges facing CMOs and CIOs. It results in jargon-free press releases and spot on pitches that</p>
  </article>

  <footer class="site-footer">
    <div class="footer-links">About Us<span>|</span>Contact Us<span>|</span>Terms &amp; Condition<span>&nbsp;|&nbsp;</span>Privacy Policy Copyright © 2014 Brimlow. All rights reserved</div>
    <div class="phone">
      <svg width="24" height="24" viewBox="0 0 24 24">
        <circle cx="12" cy="12" r="12" fill="var(--tag-red)"/>
        <path d="M9 6.5 l2 3 -1.3 1.3 q1 2.3 3.5 3.5 l1.3-1.3 3 2 -1.3 2 q-6 0-9-7z" fill="#fff"/>
      </svg>
      <span class="phone-number">555 014 2702</span>
    </div>
  </footer>
</body>
</html>
```